Design a styled business card for an intimacy and attachment psychologist

I am a Psychologist providing online therapy to patients across the United States. My work is interpersonal and emotion-focused, with an emphasis on the client-therapist relationship. My primary areas of work are very personal, including sexuality and gender, abuse and trauma, and grief and loss. My target audience will be adults of all ages 18+.
My business card should convey a warm and inviting feeling of professionalism that is also casual and comfortable.
The front should be fairly simple and professional, consisting of:
- My name, Dr. Rosalind Petrakis
- My title, Licensed Psycholigist
- My logo
On either the front or the back, my contact information should be listed:
- ros@drrospetrakis.example
- 555.014.7788
- drrospetrakis.example
On the rear, I would like a description of the areas that I specialize in. This can be formatted in any way that appears stylistically interesting.
Individual and Couples
Relationships and Infidelity
Sexual Health & Aging
Gender Identity & Sexual Orientation
Abuse and Trauma
Sexual Compulsivity & Addiction
Sexual Dysfunction
Target Market(s)
My target audience will be adults of all ages 18+.
Industry/Entity Type
Psychology
Contact Information for Business Card
The front should be fairly simple and professional, consisting of: - My name, Dr. Rosalind Petrakis - My title, Licensed Psycholigist - My logo On either the front or the back, my contact information should be listed: - ros@drrospetrakis.example - 555.014.7788 - drrospetrakis.example On the rear, I would like a description of the areas that I specialize in. This can be formatted in any way that appears stylistically interesting. Individual and Couples Relationships and Infidelity Sexual Health & Aging Gender Identity & Sexual Orientation Abuse and Trauma Sexual Compulsivity & Addiction Sexual Dysfunction
- Follow brand guide

```html
<!DOCTYPE html>
<html lang="en">
<head>
<meta charset="utf-8">
<title>Dr. Rosalind Petrakis – Business Card</title>
<link rel="stylesheet" href="https://fonts.googleapis.com/css2?family=Cinzel:wght@500;600&family=Poppins:wght@400;500&display=swap">
<style>
  :root {
    --stage: #3a3a3c;
    --ink: #2b2450;
    --paper: #ffffff;
    --violet: #9b4fb5;
    --amber: #f7a21b;
    --coral: #f0424a;
    --mint: #3fd1b0;
    --rule: #8b86a6;
  }
  * { box-sizing: border-box; margin: 0; padding: 0; }
  html, body { width: 1200px; height: 689px; overflow: hidden; }
  body {
    background: var(--stage);
    position: relative;
    font-family: "Poppins", sans-serif;
  }
  .card {
    position: absolute;
    top: 190px;
    width: 540px;
    height: 309px;
    border-radius: 18px;
    overflow: hidden;
    box-shadow: 0 14px 30px rgba(0,0,0,.35);
  }
  .card--back { left: 40px; background: var(--ink); color: #fff; }
  .card--front { left: 620px; background: var(--paper); color: var(--ink); }
  .card__waves { position: absolute; inset: 0; width: 100%; height: 100%; }

  .brand {
    position: absolute;
    left: 28px;
    top: 62px;
    width: 170px;
    text-align: center;
  }
  .brand__mark {
    width: 74px; height: 74px;
    border-radius: 50%;
    margin: 0 auto 12px;
  }
  .card--back .brand__mark { background: var(--mint); border: 3px solid #fff; }
  .card--front .brand__mark { background: var(--mint); border: 3px solid var(--ink); }
  .brand__name {
    font-family: "Cinzel", serif;
    font-weight: 600;
    line-height: 1.02;
    font-size: 26px;
  }
  .brand__name small { display: block; font-size: 16px; }
  .card--back .brand__name { color: #fff; }
  .card--front .brand__name { color: var(--ink); }

  .divider {
    position: absolute;
    left: 190px;
    top: 70px;
    width: 1px;
    height: 150px;
    background: var(--rule);
  }

  .specialties {
    position: absolute;
    left: 210px;
    top: 48px;
    list-style: none;
    font-size: 12px;
    line-height: 21px;
  }
  .specialties li { display: flex; align-items: center; gap: 9px; white-space: nowrap; }
  .specialties li::before {
    content: "";
    width: 10px; height: 10px;
    border-radius: 50%;
    background: var(--mint);
    border: 1.5px solid #fff;
    flex: none;
  }

  .identity { position: absolute; left: 212px; top: 72px; }
  .identity__name {
    font-family: "Cinzel", serif;
    font-weight: 600;
    font-size: 17px;
    letter-spacing: .3px;
  }
  .identity__title { font-size: 12px; margin-top: 1px; }
  .contacts { list-style: none; margin-top: 22px; font-size: 12.5px; line-height: 22px; }
  .contacts li { display: flex; align-items: center; gap: 8px; }
  .contacts svg { width: 12px; height: 12px; fill: var(--ink); flex: none; }
</style>
</head>
<body>

<section class="card card--back" aria-label="Card back: areas of practice">
  <svg class="card__waves" viewBox="0 0 540 309" preserveAspectRatio="none" aria-hidden="true">
    <path fill="var(--amber)" d="M0 280 C200 276 330 236 420 158 C470 112 505 86 540 80 L540 309 L0 309 Z"/>
    <path fill="var(--violet)" d="M0 295 C200 290 330 250 420 170 C470 122 505 97 540 92 L540 309 L0 309 Z"/>
    <path fill="none" stroke="var(--coral)" stroke-width="3" d="M150 291 C260 280 350 236 420 170 C470 122 505 97 540 92"/>
  </svg>

  <div class="brand">
    <div class="brand__mark"></div>
    <p class="brand__name"><small>Dr.</small>Rosalind Petrakis</p>
  </div>
  <div class="divider"></div>

  <ul class="specialties">
    <li>Individual and Couples</li>
    <li>Relationships and Infidelity</li>
    <li>Sexual Health &amp; Aging</li>
    <li>Gender Identity &amp; Sexual Orientation</li>
    <li>Abuse and Trauma</li>
    <li>Sexual Compulsivity &amp; Addiction</li>
    <li>Sexual Dysfunction</li>
  </ul>
</section>

<section class="card card--front" aria-label="Card front: name and contact">
  <svg class="card__waves" viewBox="0 0 540 309" preserveAspectRatio="none" aria-hidden="true">
    <path fill="var(--violet)" d="M60 309 C260 300 410 262 470 196 C505 156 522 128 540 118 L540 309 Z"/>
    <path fill="var(--ink)" d="M150 309 C320 300 420 262 480 192 C510 152 525 136 540 132 L540 309 Z"/>
    <path fill="none" stroke="var(--mint)" stroke-width="3" d="M150 309 C320 300 420 262 480 192 C510 152 525 136 540 132"/>
  </svg>

  <div class="brand">
    <div class="brand__mark"></div>
    <p class="brand__name"><small>Dr.</small>Rosalind Petrakis</p>
  </div>
  <div class="divider"></div>

  <div class="identity">
    <h1 class="identity__name">DR. ROSALIND PETRAKIS</h1>
    <p class="identity__title">Licensed Psycholigist</p>
    <ul class="contacts">
      <li><svg viewBox="0 0 24 24"><path d="M6.6 10.8a15.1 15.1 0 0 0 6.6 6.6l2.2-2.2a1 1 0 0 1 1-.25 11.4 11.4 0 0 0 3.6.57 1 1 0 0 1 1 1V20a1 1 0 0 1-1 1A17 17 0 0 1 3 4a1 1 0 0 1 1-1h3.5a1 1 0 0 1 1 1c0 1.25.2 2.45.57 3.57a1 1 0 0 1-.25 1z"/></svg>555.014.7788</li>
      <li><svg viewBox="0 0 24 24"><path d="M2 5h20v14H2z M2 5l10 8 10-8" fill="var(--ink)"/><path d="M3 6l9 7 9-7" fill="none" stroke="#fff" stroke-width="1.6"/></svg>ros@drrospetrakis.example</li>
      <li><svg viewBox="0 0 24 24"><circle cx="12" cy="12" r="10"/><path d="M2 12h20M12 2c3 3 3 17 0 20M12 2c-3 3-3 17 0 20" fill="none" stroke="#fff" stroke-width="1.4"/></svg>drrospetrakis.example</li>
    </ul>
  </div>
</section>

</body>
</html>
```